Simple AD for Digital Publication

Total Size 5" x 5", may include boarder or not
Image Provided; crop or use as background
Incorporate Logo and text as provided

Target Market(s)

Sound Contractors / Integrators

Industry/Entity Type

Audio Video Lighting

Requirements
Must have
• Bold Look that reflects our brand. see website: tovermundic.com - cohesive text and style

```html
<!DOCTYPE html>
<html lang="en">
<head>
<meta charset="utf-8">
<title>Tovermund Stageworks – Become a Dealer</title>
<link href="https://fonts.googleapis.com/css2?family=Montserrat:ital,wght@0,400;0,700;0,800;1,700;1,800&display=swap" rel="stylesheet">
<style>
  :root {
    --backdrop: #404040;
    --paper: #ffffff;
    --panel-top: #f4f4f4;
    --panel-bottom: #e9e9e9;
    --ink: #2e2e2e;
    --brand-red: #b01e23;
    --white: #ffffff;
  }
  * { margin: 0; padding: 0; box-sizing: border-box; }
  html, body {
    width: 1200px; height: 1200px; overflow: hidden;
    background: var(--backdrop);
    font-family: "Montserrat", Arial, sans-serif;
  }
  .ad {
    position: absolute; left: 162px; top: 162px;
    width: 878px; height: 878px;
    background: linear-gradient(180deg, var(--panel-top), var(--panel-bottom));
  }
  .ad-header {
    position: absolute; left: 0; top: 0; width: 100%; height: 145px;
    background: var(--paper);
    display: flex; align-items: center; justify-content: center; gap: 18px;
  }
  .brand-mark {
    width: 46px; height: 46px; background: var(--brand-red);
  }
  .brand-text { display: flex; flex-direction: column; }
  .brand-name {
    font-weight: 800; font-size: 38px; line-height: 1;
    color: var(--ink); letter-spacing: -0.5px;
  }
  .brand-tagline {
    margin-top: 6px; font-weight: 700; font-size: 18px;
    color: var(--ink);
  }
  .headline {
    position: absolute; left: 0; top: 178px; width: 100%;
    text-align: center; font-weight: 800; font-style: italic;
    font-size: 51px; line-height: 56px; color: var(--ink);
  }
  .headline .accent { color: var(--brand-red); }
  .photo-frame {
    position: absolute; left: 77px; top: 378px;
    width: 723px; height: 407px;
    border: 6px solid var(--brand-red);
  }
  .photo {
    position: absolute; left: 13px; top: 12px; right: 13px; bottom: 12px;
    background: linear-gradient(180deg, #2f5a2a 0%, #4f6b34 30%, #a79a9c 45%, #c2b2b6 75%, #d4c7ca 100%);
  }
  .cta {
    position: absolute; left: 211px; top: 739px;
    width: 456px; height: 83px; border-radius: 42px;
    background: var(--brand-red);
    display: flex; align-items: center;
    text-decoration: none;
  }
  .cta-icon { margin-left: 19px; width: 48px; height: 48px; }
  .cta-label {
    margin-left: 32px; color: var(--white);
    font-weight: 400; font-size: 28px; letter-spacing: 0.3px;
  }
</style>
</head>
<body>
  <main class="ad">
    <header class="ad-header">
      <div class="brand-mark"></div>
      <div class="brand-text">
        <span class="brand-name">TOVERMUND STAGEWORKS</span>
        <span class="brand-tagline">Stage Pocket Systems Connectivity</span>
      </div>
    </header>

    <h1 class="headline">
      PROTECT AND CONCEAL<br>
      <span class="accent">HIGH</span> AND <span class="accent">LOW</span><br>
      VOLTAGE CONNECTIVITY
    </h1>

    <div class="photo-frame">
      <div class="photo" role="img" aria-label="Black stage floor pocket set into a wood stage floor with cables running out, beside a lit evergreen garland"></div>
    </div>

    <a class="cta" href="https://tovermundic.com">
      <svg class="cta-icon" viewBox="0 0 48 48" aria-hidden="true">
        <circle cx="24" cy="24" r="24" fill="#ffffff"/>
        <path d="M12 20h12v-7l12 11-12 11v-7H12z" fill="#b01e23"/>
      </svg>
      <span class="cta-label">BECOME A DEALER</span>
    </a>
  </main>
</body>
</html>
```